Brindle 48 Focus Wheel

We need a professional **framework wheel diagram** designed for our detection dog training manual.

Our business is **Brindle 48 Dog Training**, and this graphic represents our **Detection Training Model**.

Please use the **attached reference images** as a guide for the structure and layout of the wheel.

### What we need

1. **Full wheel graphic**

* Clean circular framework wheel
* Similar structure to the attached example
* Clear sections and text
* Professional training manual style
* Transparent background

2. **Individual segment pieces**

We also need the **inner sections broken into separate pieces** (like the second reference image).

This will allow us to place each section on different pages of the manual when explaining the concepts.

Each piece should look like a **slice of the wheel**.

### Style

The design should look:

• Professional
• Clean and modern
• Structured and easy to read
• Suitable for a training manual

Avoid cartoon styles or clipart.

### Colours

Please use our brand colour palette (see attached image):

* Dark navy blue
* Steel blue
* Light blue
* White
* Light grey
* Dark grey

### Files required

Final files must include:

* Vector files (AI or EPS)
* Transparent PNG
* High-resolution PDF

Please also provide **each segment exported individually**

```html
<!DOCTYPE html>
<html lang="en">
<head>
<meta charset="utf-8">
<title>Brindle 48 Focus Wheel</title>
<link rel="stylesheet" href="https://fonts.googleapis.com/css2?family=Barlow:wght@500;600&family=Barlow+Condensed:wght@600;700&display=swap">
<style>
  :root {
    --steel: #5cb6c8;
    --sky: #85e7f0;
    --navy: #1e3a4a;
    --rule: #4a585c;
    --paper: #ffffff;
    --white: #ffffff;
  }
  html, body {
    margin: 0;
    padding: 0;
    width: 1200px;
    height: 1165px;
    overflow: hidden;
    background: var(--paper);
  }
  .focus-wheel { display: block; width: 1200px; height: 1165px; }

  .seg { stroke-width: 16; stroke-linejoin: round; }
  .seg-dark { fill: var(--steel); stroke: var(--steel); }
  .seg-light { fill: var(--sky); stroke: var(--sky); }

  .cycle-line { fill: none; stroke: var(--rule); stroke-width: 6; stroke-linecap: round; stroke-linejoin: round; }
  .cycle-dot { fill: var(--rule); }
  .foundation-rule { fill: none; stroke: var(--rule); stroke-width: 7; }

  .ring-title {
    font-family: "Barlow", sans-serif;
    font-weight: 600;
    fill: var(--steel);
  }
  .ring-title--outer { font-size: 84px; }
  .ring-title--middle { font-size: 70px; }
  .ring-title--hub { font-size: 46px; }

  .area-label {
    font-family: "Barlow", sans-serif;
    font-weight: 600;
    fill: var(--white);
  }
  .area-label--top { font-size: 50px; letter-spacing: 4px; }
  .area-label--bottom { font-size: 52px; letter-spacing: 7px; }
  .area-label--dark { fill: var(--navy); }

  .core-label {
    font-family: "Barlow Condensed", sans-serif;
    font-weight: 700;
    fill: var(--white);
  }
  .core-label--sm { font-size: 44px; }
  .core-label--md { font-size: 48px; }
  .core-label--lg { font-size: 62px; }

  .hub-badge { fill: var(--paper); stroke: var(--rule); stroke-width: 3; }
  .hub-name {
    font-family: "Barlow Condensed", sans-serif;
    font-weight: 700;
    font-size: 42px;
    fill: var(--navy);
  }
</style>
</head>
<body>
<svg class="focus-wheel" viewBox="0 0 1960 1903" xmlns="http://www.w3.org/2000/svg" role="img" aria-label="Brindle 48 Focus Wheel: detection training model">
  <defs>
    <!-- segment shapes, centred on the vertical axis -->
    <path id="outer-top-seg" d="M -242.6 -794.9 A 831 831 0 0 1 242.6 -794.9 L 173.6 -582.7 A 608 608 0 0 0 -173.6 -582.7 Z"/>
    <path id="outer-bottom-seg" d="M -304.2 773.3 A 831 831 0 0 0 304.2 773.3 L 218.8 567.3 A 608 608 0 0 1 -218.8 567.3 Z"/>
    <path id="inner-top-seg" d="M -128.4 -443.8 A 462 462 0 0 1 128.4 -443.8 L 48.3 -197.2 A 203 203 0 0 0 -48.3 -197.2 Z"/>
    <path id="inner-bottom-seg" d="M -162.9 432.3 A 462 462 0 0 0 162.9 432.3 L 63.6 192.8 A 203 203 0 0 1 -63.6 192.8 Z"/>

    <!-- label guides for outer ring segments -->
    <path id="guide-area-top" d="M -606.2 -350 A 700 700 0 0 1 606.2 -350"/>
    <path id="guide-area-bottom" d="M -640.9 370 A 740 740 0 0 0 640.9 370"/>

    <!-- ring title guides -->
    <path id="guide-operational-top" d="M 142.9 803.4 A 850 850 0 0 1 1817.1 803.4"/>
    <path id="guide-operational-bottom" d="M 75.9 1110.4 A 918 918 0 0 0 1884.1 1110.4"/>
    <path id="guide-dog-foundations" d="M 519.6 783.4 A 490 490 0 0 1 1440.4 783.4"/>
    <path id="guide-handler-foundations" d="M 453.8 1142.5 A 560 560 0 0 0 1506.2 1142.5"/>
    <path id="guide-hub-top" d="M 856.9 933.3 A 125 125 0 0 1 1103.1 933.3"/>
    <path id="guide-hub-bottom" d="M 827.4 995.9 A 158 158 0 0 0 1132.6 995.9"/>
  </defs>

  <!-- operating cycle arrows -->
  <g class="cycle">
    <path class="cycle-line" d="M 36.4 899.9 A 945 945 0 0 1 1924.1 909.8"/>
    <polyline class="cycle-line" points="1890,858 1924.1,909.8 1957,858"/>
    <circle class="cycle-dot" cx="36.4" cy="899.9" r="14"/>

    <path class="cycle-line" d="M 1923.5 1003.7 A 945 945 0 1 1 36.3 1000.5"/>
    <polyline class="cycle-line" points="4,1052 36.3,1000.5 70,1052"/>
    <circle class="cycle-dot" cx="1923.5" cy="1003.7" r="14"/>
  </g>

  <!-- operational capability area titles -->
  <text class="ring-title ring-title--outer">
    <textPath href="#guide-operational-top" startOffset="50%" text-anchor="middle" textLength="1140" lengthAdjust="spacing">OPERATIONAL CAPABILITY AREA</textPath>
  </text>
  <text class="ring-title ring-title--outer">
    <textPath href="#guide-operational-bottom" startOffset="50%" text-anchor="middle" textLength="1200" lengthAdjust="spacing">OPERATIONAL CAPABILITY AREA</textPath>
  </text>

  <!-- outer ring: operational areas -->
  <g class="outer-ring" transform="translate(980 951)">
    <g transform="rotate(-72)">
      <use href="#outer-top-seg" class="seg seg-dark"/>
      <text class="area-label area-label--top"><textPath href="#guide-area-top" startOffset="50%" text-anchor="middle">INTEGRITY</textPath></text>
    </g>
    <g transform="rotate(-36)">
      <use href="#outer-top-seg" class="seg seg-dark"/>
      <text class="area-label area-label--top"><textPath href="#guide-area-top" startOffset="50%" text-anchor="middle">DEVELOPMENT</textPath></text>
    </g>
    <g>
      <use href="#outer-top-seg" class="seg seg-light"/>
      <text class="area-label area-label--top area-label--dark"><textPath href="#guide-area-top" startOffset="50%" text-anchor="middle">DISTRACTIONS</textPath></text>
    </g>
    <g transform="rotate(36)">
      <use href="#outer-top-seg" class="seg seg-dark"/>
      <text class="area-label area-label--top"><textPath href="#guide-area-top" startOffset="50%" text-anchor="middle">BEHAVIOUR</textPath></text>
    </g>
    <g transform="rotate(72)">
      <use href="#outer-top-seg" class="seg seg-dark"/>
      <text class="area-label area-label--top"><textPath href="#guide-area-top" startOffset="50%" text-anchor="middle">HANDLER</textPath></text>
    </g>

    <g transform="rotate(67.5)">
      <use href="#outer-bottom-seg" class="seg seg-light"/>
      <text class="area-label area-label--bottom area-label--dark"><textPath href="#guide-area-bottom" startOffset="50%" text-anchor="middle">DEPLOYMENT</textPath></text>
    </g>
    <g transform="rotate(22.5)">
      <use href="#outer-bottom-seg" class="seg seg-dark"/>
      <text class="area-label area-label--bottom"><textPath href="#guide-area-bottom" startOffset="50%" text-anchor="middle">REINFORCEMENT</textPath></text>
    </g>
    <g transform="rotate(-22.5)">
      <use href="#outer-bottom-seg" class="seg seg-dark"/>
      <text class="area-label area-label--bottom"><textPath href="#guide-area-bottom" startOffset="50%" text-anchor="middle">SEARCH METHOD</textPath></text>
    </g>
    <g transform="rotate(-67.5)">
      <use href="#outer-bottom-seg" class="seg seg-light"/>
      <text class="area-label area-label--bottom area-label--dark"><textPath href="#guide-area-bottom" startOffset="50%" text-anchor="middle">TARGET ODOUR</textPath></text>
    </g>
  </g>

  <!-- foundation rules and titles -->
  <g class="foundation-rules" transform="translate(980 951)">
    <path class="foundation-rule" d="M -357.6 -411.3 A 545 545 0 0 0 -417.5 350.3"/>
    <path class="foundation-rule" d="M 417.5 350.3 A 545 545 0 0 0 357.6 -411.3"/>
  </g>
  <text class="ring-title ring-title--middle">
    <textPath href="#guide-dog-foundations" startOffset="50%" text-anchor="middle" textLength="570" lengthAdjust="spacing">DOG FOUNDATIONS</textPath>
  </text>
  <text class="ring-title ring-title--middle">
    <textPath href="#guide-handler-foundations" startOffset="50%" text-anchor="middle" textLength="810" lengthAdjust="spacing">HANDLER FOUNDATIONS</textPath>
  </text>

  <!-- inner wheel: foundations -->
  <g class="inner-wheel" transform="translate(980 951)">
    <use href="#inner-top-seg" class="seg seg-dark" transform="rotate(-72)"/>
    <use href="#inner-top-seg" class="seg seg-dark" transform="rotate(-36)"/>
    <use href="#inner-top-seg" class="seg seg-dark"/>
    <use href="#inner-top-seg" class="seg seg-dark" transform="rotate(36)"/>
    <use href="#inner-top-seg" class="seg seg-dark" transform="rotate(72)"/>
    <use href="#inner-bottom-seg" class="seg seg-light" transform="rotate(67.5)"/>
    <use href="#inner-bottom-seg" class="seg seg-light" transform="rotate(22.5)"/>
    <use href="#inner-bottom-seg" class="seg seg-light" transform="rotate(-22.5)"/>
    <use href="#inner-bottom-seg" class="seg seg-light" transform="rotate(-67.5)"/>
  </g>

  <g class="core-labels">
    <text class="core-label core-label--sm" text-anchor="end"><tspan x="737" y="866">GENETIC</tspan><tspan x="737" y="914">SUITABILITY</tspan></text>
    <text class="core-label core-label--sm" text-anchor="middle"><tspan x="767" y="640">HEALTH &amp;</tspan><tspan x="767" y="688">PHYSICAL</tspan><tspan x="767" y="736">WELLBEING</tspan></text>
    <text class="core-label core-label--sm" text-anchor="middle"><tspan x="978" y="564">ENGAGEMENT</tspan><tspan x="978" y="610">RELATIONSHIP</tspan></text>
    <text class="core-label core-label--sm" text-anchor="middle"><tspan x="1187" y="682">REWARD</tspan><tspan x="1187" y="730">VALUE</tspan></text>
    <text class="core-label core-label--sm"><tspan x="1220" y="866">AROUSAL</tspan><tspan x="1220" y="914">REGULATION</tspan></text>

    <text class="core-label core-label--lg" text-anchor="end"><tspan x="737" y="1052">DOG</tspan><tspan x="737" y="1118">SAFETY</tspan></text>
    <text class="core-label core-label--lg" text-anchor="middle"><tspan x="852" y="1244">SEARCH</tspan><tspan x="852" y="1310">COVERAGE</tspan></text>
    <text class="core-label core-label--md" text-anchor="middle"><tspan x="1110" y="1220">MINIMAL</tspan><tspan x="1110" y="1276">NECESSARY</tspan><tspan x="1110" y="1332">INVOLVEMENT</tspan></text>
    <text class="core-label core-label--lg"><tspan x="1200" y="1052">READ</tspan><tspan x="1200" y="1118">THE DOG</tspan></text>
  </g>

  <!-- hub -->
  <text class="ring-title ring-title--hub">
    <textPath href="#guide-hub-top" startOffset="50%" text-anchor="middle" textLength="255" lengthAdjust="spacing">DETECTION</textPath>
  </text>
  <text class="ring-title ring-title--hub">
    <textPath href="#guide-hub-bottom" startOffset="50%" text-anchor="middle" textLength="370" lengthAdjust="spacing">CAPABILITIES</textPath>
  </text>
  <g class="hub-brand">
    <circle class="hub-badge" cx="980" cy="965" r="92"/>
    <text class="hub-name" x="980" y="980" text-anchor="middle">Brindle 48</text>
  </g>
</svg>
</body>
</html>
```